Company Presentation / Image Presentation

Take the file attached and transform it into a modern and compelling design; fitting to the concepts and design language of our Homepage (lomtrive.net) - but not just copy it - do an interpretation. We expect in the first step a Powerpoint - second step (not part on tis here) a Flyer. We will set up a second request.

Target Market(s)

Corporate companies across Europe

Industry/Entity Type

Corporate

Font styles to use
Sans Serif

Colors
3277b5
33a6d7
33b8a4

Requirements
Must have
• Modern style - in sync. with our HP http://www.lomtrive.net
Nice to have
• https://www.example-network.com/company/58204417
Should not have
• stupid stereotypes

```html
<!DOCTYPE html>
<html lang="en">
<head>
<meta charset="utf-8">
<title>Will Disruption &amp; Digitalization influent corporate businesses?</title>
<link href="https://fonts.googleapis.com/css2?family=Carlito:wght@400;700&family=Archivo+Narrow:wght@400&family=Montserrat:wght@200;700&display=swap" rel="stylesheet">
<style>
  :root {
    --navy: #0c1f4a;
    --teal-band: #2bb5b8;
    --sky: #33a6d7;
    --teal: #33b8a4;
    --blue: #4a78c8;
    --green: #6aa83e;
    --orange: #ee7f30;
    --white: #ffffff;
  }
  html, body { margin: 0; padding: 0; overflow: hidden; }
  body { background: var(--white); }
  .slide {
    position: relative; width: 1200px; height: 671px; overflow: hidden;
    background: var(--white); font-family: "Archivo Narrow", "Arial Narrow", sans-serif;
  }
  .decor { position: absolute; inset: 0; }
  .side-band {
    position: absolute; left: 0; top: 0; width: 42px; height: 671px; background: var(--teal-band);
  }
  .side-title {
    position: absolute; left: 21px; top: 660px; transform-origin: 0 0; transform: rotate(-90deg) translateY(-50%);
    white-space: nowrap; font-family: "Montserrat", sans-serif; font-weight: 700; font-size: 21.5px;
    color: var(--white); letter-spacing: 0.1px;
  }
  .panel {
    position: absolute; left: 42px; top: 31px; width: 1126px; height: 608px; background: var(--navy);
  }
  .tagline {
    position: absolute; left: 53px; top: 628px; transform-origin: 0 0; transform: rotate(-90deg);
    white-space: nowrap; font-family: "Montserrat", sans-serif; font-weight: 200; font-size: 17px; color: var(--white);
  }
  .headline {
    position: absolute; right: 789px; top: 158px; margin: 0; text-align: right;
    font-family: "Carlito", "Calibri", sans-serif; font-weight: 400; font-size: 48px; line-height: 58.5px;
    color: var(--sky); white-space: nowrap;
  }
  .headline .prompt { font-size: 12px; color: var(--teal); margin-right: 3px; vertical-align: 3px; line-height: 1; }
  .divider { position: absolute; left: 457px; top: 202px; width: 1px; height: 267px; background: var(--white); }
  .outlook { position: absolute; left: 0; top: 0; margin: 0; padding: 0; list-style: none; }
  .outlook li {
    position: absolute; left: 509px; width: 640px; color: var(--white); font-size: 15.4px; line-height: 18.6px;
  }
  .outlook li::before { content: "•"; position: absolute; left: -20px; top: 0; }
  .outlook .note { display: block; color: var(--teal); font-size: 9.4px; line-height: 12px; margin-top: 3px; }
</style>
</head>
<body>
<div class="slide">
  <svg class="decor" width="1200" height="671" viewBox="0 0 1200 671" aria-hidden="true">
    <rect x="672" y="0" width="7" height="40" fill="var(--green)"/>
    <polyline points="842,-8 890,20 858,44" fill="none" stroke="var(--green)" stroke-width="7" stroke-linecap="round" stroke-linejoin="round"/>
    <circle cx="1060" cy="-25" r="57" fill="var(--blue)"/>
    <circle cx="801" cy="770" r="128" fill="var(--orange)"/>
    <rect x="1160" y="402" width="40" height="11" fill="var(--green)"/>
    <rect x="1160" y="563" width="40" height="11" fill="var(--green)"/>
  </svg>

  <div class="side-band"></div>
  <div class="side-title">Transitioning corporates towards Scaled Agility…</div>

  <section class="panel"></section>
  <div class="tagline">Not more – not less.</div>

  <h1 class="headline"><span class="prompt">What do you think ?</span>Will<br>“Disruption” &amp;<br>“Digitalization”<br>influent<br>corporate<br>businesses?</h1>

  <div class="divider"></div>

  <ul class="outlook">
    <li style="top:82px">E-powering of transportation (Automobiles, Trucks and Motorcycles ) will render (min.) 60 percent of current (2018) manufacturing &amp; assembly labor obsolete.<span class="note">(an engine concept based on fossil energy holds 2600 spinning parts – an electric engine: 17)</span></li>
    <li style="top:144px">3-&amp;4D printing technology will render CNC and traditional craftsmanship 100 percent redundant.<span class="note">(Automotive OEM’s are already printing parts of their sports car braking-system in Titanium)</span></li>
    <li style="top:188px">One Trillion of permanently connected IoT-sensors (by 2030) will produce revealing real-time information and insights – about almost everything within the technology centric economic ecosystem.<span class="note">(Information is just what it is – something is currently in the process of being “in-for-mation” – almost everything will be possible with that mass of real-time data)</span></li>
    <li style="top:281px">AI-bots will produce at least 40 percent of all accessible journalistic work without engaging any human writers.<span class="note">(Expectations shifts from commodity work towards high-sophisticated quality deliveries)</span></li>
    <li style="top:343px">Commodity Banking services will be 100-percent digitalized for 80 percent of the finance customers.<span class="note">(This fact will make the effort 5 of 7 collaborators in the finance industry futile)</span></li>
    <li style="top:387px">Mass production of products will end – instant production of tailor-made, personalized and individualized one-of-a-kind-goods will become the standard in manufacturing (Lot-size one).<span class="note">(pharmaceutical remedies produced to an individuals needs will reduce waste of all kind of resources)</span></li>
    <li style="top:449px">Solar-powered Internet-connection drones will provide reliable access to the internet for more than 3 billion new-connected brains.<span class="note">(Innovation and competition on products, processes and services will create new concepts goods and solutions)</span></li>
    <li style="top:511px">Sharing Economy will completely shift the societies understanding of what ”business” and “collaboration” will be.<span class="note">(the demand on products and services shifts away from quantity towards quality)</span></li>
    <li style="top:573px">and an almost endless row of further examples more…</li>
  </ul>
</div>
</body>
</html>
```